Mobile Printer company needs a corporate PowerPoint Template

Looking to get a corporate PowerPoint template created to sue for a variety of presentations to customer, resellers, and partners. Would like the color scheme to include Blue, black, and grey to match our corporate colors. Since we are a mobile technology company, I'd like the template to have modern tech look to it. Attached is our current PowerPoint that we use for new partners.

Target Market(s)

public safety, hospitality, route accounting, DSD, warehousing/logistics, health care, etc.

Industry/Entity Type

Too many to list

Colors
0054AA
0677BA
7BADD7
CADEEF
E8F1F8

Requirements
Must have
• Tavolin logo, places to drop in photos
Nice to have
• attractive graphics to display excel data

```html
<!DOCTYPE html>
<html lang="en">
<head>
<meta charset="utf-8">
<title>Tavolin Corporate Template</title>
<link href="https://fonts.googleapis.com/css2?family=Poppins:wght@300;400;500;600;700;800&display=swap" rel="stylesheet">
<style>
:root{
  --blue:#1588d2;
  --blue-deep:#0677ba;
  --blue-soft:#7badd7;
  --blue-pale:#cadeef;
  --blue-mist:#e8f1f8;
  --ink:#111111;
  --grey:#555555;
  --grey-light:#e4e4e4;
  --canvas:#cfcfcf;
  --white:#ffffff;
}
*{margin:0;padding:0;box-sizing:border-box}
html,body{width:906px;height:1200px;overflow:hidden}
body{background:var(--canvas);font-family:"Poppins",Arial,sans-serif;color:var(--ink);position:relative}
.slide{position:absolute;width:278px;height:156px;background:var(--white);overflow:hidden;box-shadow:0 2px 4px rgba(0,0,0,.35)}
.abs{position:absolute}
.tab-right{position:absolute;right:0;top:0;width:11px;height:55px;background:var(--blue);border-bottom-left-radius:10px}
.tab-left{position:absolute;left:0;top:0;width:11px;height:55px;background:var(--blue);border-bottom-right-radius:10px}
.corner-black{position:absolute;left:0;bottom:0;width:58px;height:11px;background:var(--ink);border-top-right-radius:11px}
.corner-black-top{position:absolute;left:0;top:0;width:58px;height:11px;background:var(--ink);border-bottom-right-radius:11px}
.corner-black-tr{position:absolute;right:0;top:0;width:58px;height:11px;background:var(--ink);border-bottom-left-radius:11px}
.band-blue-bottom{position:absolute;left:0;bottom:0;width:80px;height:8px;background:var(--blue);border-top-right-radius:8px}
.foot{position:absolute;right:7px;bottom:4px;font-size:5px;font-weight:700;letter-spacing:.2px;display:flex;align-items:center;gap:1.5px}
.foot .mark{width:4px;height:4px;border:1px solid var(--ink);border-radius:1px}
.foot .pg{background:var(--blue);color:var(--white);padding:0 1.5px;font-size:4.5px}
.dots{position:absolute;width:28px;height:10px;background-image:radial-gradient(circle,var(--blue) .6px,transparent .8px);background-size:7px 5px}
.dots.dark{background-image:radial-gradient(circle,var(--ink) .6px,transparent .8px)}
.h-sm{font-size:9px;font-weight:500;line-height:1}
.h-lg{font-size:11px;font-weight:800;line-height:1.05}
.blue{color:var(--blue)}
.white{color:var(--white)}
.body{font-size:2.6px;line-height:3.4px;color:var(--grey)}
.body.white{color:var(--white)}
.item-title{font-size:4.8px;font-weight:600;line-height:1.2}
.photo{position:absolute}
.photo-blue{background:linear-gradient(135deg,#0b5f9c,#1a8fd8 60%,#5fb0e6)}
.photo-grey{background:linear-gradient(135deg,#dcdcdc,#bdbdbd 55%,#e9e9e9)}
.photo-device{background:linear-gradient(160deg,#f2f2f2,#b9b9b9 60%,#3a3a3a)}
.big-num{font-size:22px;font-weight:700}
.part{font-size:17px;font-weight:600}
.chart-label{font-size:3.5px;fill:var(--grey);font-family:"Poppins",sans-serif}
</style>
</head>
<body>

<!-- Row 1 -->
<section class="slide" style="left:25px;top:20px">
  <div class="photo photo-blue" role="img" aria-label="Business team reviewing documents at a desk" style="left:0;top:0;width:145px;height:156px;border-top-right-radius:20px"></div>
  <div class="abs" style="left:11px;bottom:9px;font-size:5.5px;letter-spacing:2px;color:var(--white)">www.tavolin.com</div>
  <div class="abs" style="left:158px;top:60px;display:flex;align-items:center;gap:4px">
    <span style="width:7px;height:7px;background:var(--blue)"></span>
    <span style="font-size:18px;font-weight:700">TAVOLIN</span>
  </div>
  <div class="abs" style="left:169px;top:83px;font-size:6.5px;line-height:8px">Premier Mobile Printing<br>Solutions</div>
  <div class="tab-right" style="height:60px"></div>
  <div class="dots" style="left:225px;top:18px"></div>
  <div class="abs" style="left:220px;top:120px;width:58px;height:36px;background:var(--blue-mist);border-top-left-radius:18px"></div>
</section>

<section class="slide" style="left:315px;top:20px">
  <div class="corner-black-top"></div>
  <div class="tab-right"></div>
  <div class="dots" style="left:192px;top:20px"></div>
  <div class="abs blue" style="left:16px;top:22px;font-size:13px;font-weight:600">Contents</div>
  <div class="abs" style="left:16px;top:49px;width:70px">
    <div class="item-title"><span class="blue">1.</span> Lorem ipsum</div><div class="body">Lorem ipsum dolor sit amet, consec-<br>tetuer adipiscing elit, sed diam nonum-</div>
    <div class="item-title" style="margin-top:9px"><span class="blue">2. Lorem ipsum</span></div><div class="body">Lorem ipsum dolor sit amet, consec-<br>tetuer adipiscing elit, sed diam nonum-</div>
    <div class="item-title" style="margin-top:9px"><span class="blue">3.</span> Lorem ipsum</div><div class="body">Lorem ipsum dolor sit amet, consec-<br>tetuer adipiscing elit, sed diam nonum-</div>
  </div>
  <div class="abs" style="left:91px;top:49px;width:70px">
    <div class="item-title"><span class="blue">1.</span> Lorem ipsum</div><div class="body">Lorem ipsum dolor sit amet, consec-<br>tetuer adipiscing elit, sed diam nonum-</div>
    <div class="item-title" style="margin-top:9px"><span class="blue">2. Lorem ipsum</span></div><div class="body">Lorem ipsum dolor sit amet, consec-<br>tetuer adipiscing elit, sed diam nonum-</div>
    <div class="item-title" style="margin-top:9px"><span class="blue">3.</span> Lorem ipsum</div><div class="body">Lorem ipsum dolor sit amet, consec-<br>tetuer adipiscing elit, sed diam nonum-</div>
  </div>
  <div class="photo photo-device" role="img" aria-label="Three mobile receipt printers" style="left:170px;top:46px;width:88px;height:78px;border-radius:6px"></div>
  <div class="abs" style="left:63px;bottom:0;width:99px;height:10px;background:var(--blue);border-radius:8px 8px 0 0"></div>
  <div class="foot"><span class="mark"></span>TAVOLIN<span class="pg">02</span></div>
</section>

<section class="slide" style="left:605px;top:20px">
  <div class="photo photo-grey" role="img" aria-label="Faded photo of a person paying with a card and phone" style="left:0;top:0;width:278px;height:156px"></div>
  <div class="tab-right"></div>
  <div class="abs" style="left:0;bottom:0;width:12px;height:65px;background:var(--ink);border-top-right-radius:10px"></div>
  <div class="dots" style="left:208px;top:20px"></div>
  <div class="abs" style="left:118px;top:28px;width:56px;height:56px;border:4px solid var(--blue);border-radius:50%"></div>
  <div class="abs big-num" style="left:130px;top:38px">01</div>
  <div class="abs part" style="left:100px;top:112px">Part One.</div>
  <div class="foot"><span class="mark"></span>TAVOLIN<span class="pg">03</span></div>
</section>

<!-- Row 2 -->
<section class="slide" style="left:25px;top:188px">
  <div class="abs" style="left:0;top:14px;width:145px;height:142px;background:var(--blue);border-top-right-radius:22px"></div>
  <div class="abs h-sm white" style="left:17px;top:25px;font-size:10px">ABOUT OUR</div>
  <div class="abs" style="left:17px;top:36px;font-size:15px;font-weight:800">COMPANY</div>
  <div class="abs body white" style="left:17px;top:57px;width:95px">Lorem ipsum dolor sit amet, consectetuer adipiscing elit, sed diam nonummy nibh euismod tincidunt ut laoreet dolore magna aliquam erat volutpat. Ut wisi enim ad minim veniam, quis nostrud exerci tation ullamcorper suscipit lobortis nisl ut aliquip ex ea commodo consequat. Duis autem vel eum iriure dolor in hendrerit in vulputate velit esse molestie consequat.</div>
  <div class="abs body white" style="left:17px;top:107px;width:95px">Lorem ipsum dolor sit amet, cons ectetuer adipiscing elit, sed diam nonummy nibh euismod tincidunt ut laoreet dolore magna aliquam erat volutpat. Ut wisi enim ad minim veniam.</div>
  <div class="abs" style="left:133px;top:28px;width:22px;height:22px;border-radius:50%;background:var(--ink);border:2px solid var(--white);box-shadow:0 0 0 1px var(--grey-light)"></div>
  <div class="abs" style="left:133px;top:70px;width:22px;height:22px;border-radius:50%;background:var(--ink);border:2px solid var(--white)"></div>
  <div class="abs" style="left:133px;top:110px;width:22px;height:22px;border-radius:50%;background:var(--ink);border:2px solid var(--white)"></div>
  <div class="abs" style="left:161px;top:25px;width:90px"><div class="item-title">Lorem ipsum</div><div class="body">ipsum dolor sit amet, cons ectetuer adipiscing elit, sed diam nonummy nibh euismod tincidunt ut laoreet dolore magna aliquam erat volutpat.</div></div>
  <div class="abs" style="left:161px;top:67px;width:90px"><div class="item-title">Lorem ipsum</div><div class="body">ipsum dolor sit amet, cons ectetuer adipiscing elit, sed diam nonummy nibh euismod tincidunt ut laoreet dolore magna aliquam erat volutpat.</div></div>
  <div class="abs" style="left:161px;top:107px;width:90px"><div class="item-title">Lorem ipsum</div><div class="body">ipsum dolor sit amet, cons ectetuer adipiscing elit, sed diam nonummy nibh euismod tincidunt ut laoreet dolore magna aliquam erat volutpat.</div></div>
  <div class="corner-black-tr" style="width:11px;height:55px;border-radius:0 0 0 10px"></div>
  <div class="dots" style="left:220px;top:8px"></div>
  <div class="foot"><span class="mark"></span>TAVOLIN<span class="pg">04</span></div>
</section>

<section class="slide" style="left:315px;top:188px">
  <div class="abs h-sm" style="left:10px;top:11px;font-size:10px">OUR COMPANY <span class="blue" style="font-weight:700">EDUCATION</span></div>
  <div class="dots" style="left:232px;top:8px"></div>
  <div class="tab-right" style="top:22px"></div>
  <svg class="abs" style="left:0;top:0" width="278" height="156" viewBox="0 0 278 156">
    <g fill="none" stroke="#111" stroke-width="1.6">
      <path d="M52 42h38v14a4 4 0 0 1 0 8v44H52z" />
      <path d="M115 42h38v14a4 4 0 0 1 0 8v44h-38z" />
    </g>
    <path d="M178 42h46v70h-46z" fill="none" stroke="#1588d2" stroke-width="1.6"/>
    <circle cx="98" cy="58" r="2" fill="#111"/><circle cx="161" cy="58" r="2" fill="#111"/>
    <path d="M92 58h6M155 58h6" stroke="#111" stroke-width="1"/>
  </svg>
  <div class="abs blue" style="left:52px;top:64px;width:38px;text-align:center;font-size:4.5px;font-weight:600">IDEA</div>
  <div class="abs blue" style="left:115px;top:64px;width:38px;text-align:center;font-size:4.5px;font-weight:600">PROMOTION</div>
  <div class="abs blue" style="left:178px;top:64px;width:46px;text-align:center;font-size:4.5px;font-weight:600">GROWTH</div>
  <div class="abs body" style="left:55px;top:72px;width:33px;text-align:center">Lorem ipsum dolor sit amet, consectetuer adipiscing elit, sed diam nonummy nibh euismod tincidunt ut laoreet.</div>
  <div class="abs body" style="left:118px;top:72px;width:33px;text-align:center">Lorem ipsum dolor sit amet, consectetuer adipiscing elit, sed diam nonummy nibh euismod tincidunt ut laoreet.</div>
  <div class="abs body" style="left:183px;top:72px;width:36px;text-align:center">Lorem ipsum dolor sit amet, consectetuer adipiscing elit, sed diam nonummy nibh euismod tincidunt ut laoreet.</div>
  <div class="abs body" style="left:36px;top:122px;width:206px;text-align:center">Lorem ipsum dolor sit amet, consectetuer adipiscing elit, sed diam nonummy nibh euismod tincidunt ut laoreet dolore magna aliquam erat volutpat. Ut wisi enim ad minim veniam, quis nostrud exerci tation ullamcorper suscipit lobortis nisl ut aliquip ex ea commodo consequat.</div>
  <div class="corner-black"></div>
  <div class="foot"><span class="mark"></span>TAVOLIN<span class="pg">05</span></div>
</section>

<section class="slide" style="left:605px;top:188px">
  <div class="abs h-sm" style="left:12px;top:10px;font-size:10px">MARKET</div>
  <div class="abs blue" style="left:12px;top:20px;font-size:11px;font-weight:700">OPPORTUNITIES</div>
  <div class="abs body" style="left:12px;top:37px;width:120px">Lorem ipsum dolor sit amet, consectetuer adipiscing elit, sed diam nonummy nibh euismod tincidunt ut laoreet dolore magna aliquam erat volutpat. Ut wisi enim ad minim veniam, quis nostrud exerci tation ullamcorper suscipit lobortis nisl ut aliquip ex ea commodo consequat.<br><br>Lorem ipsum dolor sit amet, consectetuer adipiscing elit, sed diam nonummy nibh euismod tincidunt ut laoreet dolore magna aliquam erat volutpat.</div>
  <div class="abs blue" style="left:153px;top:20px;font-size:3.4px">CONSECTETUER ADIPISCING</div>
  <svg class="abs" style="left:0;top:0" width="278" height="156" viewBox="0 0 278 156">
    <g stroke="#ddd" stroke-width=".4"><path d="M153 29h110M153 37h110M153 45h110M153 53h110M153 61h110M153 69h110M153 77h110"/></g>
    <g class="chart-label" font-size="3.3"><text x="146" y="30">60</text><text x="146" y="38">50</text><text x="146" y="46">40</text><text x="146" y="54">30</text><text x="146" y="62">20</text><text x="146" y="70">10</text><text x="147" y="78">0</text>
    <text x="163" y="84">JAN</text><text x="185" y="84">FEB</text><text x="206" y="84">MAR</text><text x="228" y="84">APR</text></g>
    <rect x="161" y="45" width="11" height="32" fill="#1588d2"/>
    <rect x="183" y="31" width="11" height="46" fill="#111"/>
    <rect x="205" y="65" width="11" height="12" fill="#1588d2"/>
    <rect x="227" y="40" width="11" height="37" fill="#111"/>
    <ellipse cx="66" cy="118" rx="38" ry="14" fill="#0b5f9c"/>
    <path d="M66 110 L28 110 A38 20 0 0 1 66 90 Z" fill="#1588d2"/>
    <path d="M66 110 L66 90 A38 20 0 0 1 104 110 Z" fill="#111"/>
    <path d="M66 110 L104 110 A38 20 0 0 1 66 130 Z" fill="#1588d2"/>
    <path d="M66 110 L66 130 A38 20 0 0 1 28 110 Z" fill="#1588d2"/>
    <path d="M66 110 L66 130 A38 20 0 0 0 100 118 Z" fill="#111"/>
    <ellipse cx="66" cy="110" rx="12" ry="5" fill="#fff"/>
    <g font-family="Poppins" font-weight="700" font-size="6" fill="#fff"><text x="36" y="106">40%</text><text x="70" y="98">20%</text><text x="88" y="108">20%</text><text x="68" y="125">20%</text></g>
  </svg>
  <div class="abs" style="left:128px;top:96px;width:130px;display:grid;grid-template-columns:1fr 1fr;gap:5px 6px">
    <div><div class="item-title blue" style="font-size:4px">● Lorem ipsum</div><div class="body">Lorem ipsum dolor sit amet, consectetuer adipiscing elit, sed diam nonummy.</div></div>
    <div><div class="item-title" style="font-size:4px">● Lorem ipsum</div><div class="body">Lorem ipsum dolor sit amet, consectetuer adipiscing elit, sed diam nonummy.</div></div>
    <div><div class="item-title" style="font-size:4px">● Lorem ipsum</div><div class="body">Lorem ipsum dolor sit amet, consectetuer adipiscing elit, sed diam nonummy.</div></div>
    <div><div class="item-title blue" style="font-size:4px">● Lorem ipsum</div><div class="body">Lorem ipsum dolor sit amet, consectetuer adipiscing elit, sed diam nonummy.</div></div>
  </div>
  <div class="tab-right" style="top:20px"></div>
  <div class="corner-black"></div>
  <div class="dots" style="left:232px;top:8px"></div>
  <div class="foot"><span class="mark"></span>TAVOLIN<span class="pg">06</span></div>
</section>

<!-- Row 3 -->
<section class="slide" style="left:25px;top:356px">
  <div class="abs h-sm" style="left:12px;top:10px;font-size:9px;line-height:10px">PRODUCT<br>FEATURES AND</div>
  <div class="abs blue" style="left:12px;top:29px;font-size:10px;font-weight:700">FUNCTIONALITY</div>
  <div class="abs body" style="left:12px;top:43px;width:108px">Lorem ipsum dolor sit amet, consectetuer adipiscing elit, sed diam nonummy nibh euismod tincidunt ut laoreet dolore magna aliquam erat volutpat. Ut wisi enim ad minim veniam, quis nostrud exerci tation ullamcorper suscipit lobortis nisl ut aliquip ex ea commodo consequat.<br><br>Lorem ipsum dolor sit amet, consectetuer adipiscing elit, sed diam nonummy nibh.</div>
  <svg class="abs" style="left:0;top:0" width="278" height="156" viewBox="0 0 278 156">
    <g stroke="#ddd" stroke-width=".4"><path d="M146 12h112M146 21h112M146 30h112M146 39h112M146 48h112M146 57h112M146 66h112"/></g>
    <g class="chart-label" font-size="3.3"><text x="139" y="13">60</text><text x="139" y="22">50</text><text x="139" y="31">40</text><text x="139" y="40">30</text><text x="139" y="49">20</text><text x="139" y="58">10</text><text x="140" y="67">0</text>
    <text x="159" y="73">JAN</text><text x="184" y="73">FEB</text><text x="208" y="73">MAR</text><text x="233" y="73">APR</text></g>
    <rect x="157" y="30" width="3.5" height="36" fill="#1588d2"/><rect x="163" y="20" width="3.5" height="46" fill="#111"/>
    <rect x="183" y="56" width="3.5" height="10" fill="#1588d2"/><rect x="189" y="34" width="3.5" height="32" fill="#111"/>
    <rect x="208" y="14" width="3.5" height="52" fill="#1588d2"/><rect x="214" y="54" width="3.5" height="12" fill="#111"/>
    <rect x="233" y="19" width="3.5" height="47" fill="#111"/><rect x="239" y="39" width="3.5" height="27" fill="#1588d2"/>
    <g stroke="#ddd" stroke-width=".4"><path d="M22 88h112M22 95h112M22 102h112M22 109h112M22 116h112M22 123h112M22 130h112"/></g>
    <g class="chart-label" font-size="3"><text x="14" y="89">60</text><text x="14" y="96">50</text><text x="14" y="103">40</text><text x="14" y="110">30</text><text x="14" y="117">20</text><text x="14" y="124">10</text><text x="15" y="131">0</text></g>
    <polyline points="25,123 36,128 47,116 58,98 70,108 81,112 92,121 103,115 114,108 124,129" fill="none" stroke="#111" stroke-width=".8"/>
    <polyline points="25,128 36,120 47,110 58,112 70,105 81,118 92,110 103,116 114,112 124,105" fill="none" stroke="#1588d2" stroke-width=".8"/>
  </svg>
  <div class="abs" style="left:152px;top:90px;width:115px;display:grid;grid-template-columns:1fr 1fr;gap:6px 8px">
    <div><div class="item-title blue" style="font-size:4px">● Lorem ipsum</div><div class="body">Lorem ipsum dolor sit amet, consectetuer adipiscing elit, sed diam nonummy.</div></div>
    <div><div class="item-title" style="font-size:4px">● Lorem ipsum</div><div class="body">Lorem ipsum dolor sit amet, consectetuer adipiscing elit, sed diam nonummy.</div></div>
    <div><div class="item-title" style="font-size:4px">● Lorem ipsum</div><div class="body">Lorem ipsum dolor sit amet, consectetuer adipiscing elit, sed diam nonummy.</div></div>
    <div><div class="item-title blue" style="font-size:4px">● Lorem ipsum</div><div class="body">Lorem ipsum dolor sit amet, consectetuer adipiscing elit, sed diam nonummy.</div></div>
  </div>
  <div class="tab-right"></div>
  <div class="corner-black" style="width:58px"></div>
  <div class="foot"><span class="mark"></span>TAVOLIN<span class="pg">07</span></div>
</section>

<section class="slide" style="left:315px;top:356px">
  <div class="corner-black-top"></div>
  <div class="tab-right" style="top:20px"></div>
  <div class="dots" style="left:232px;top:8px"></div>
  <div class="abs" style="left:16px;top:22px;font-size:13px;font-weight:600;line-height:1">MARKET</div>
  <div class="abs blue" style="left:16px;top:37px;font-size:14px;font-weight:700">OPPORTUNITIES</div>
  <div class="abs body" style="left:16px;top:58px;width:105px">Lorem ipsum dolor sit amet, consectetuer adipiscing elit, sed diam nonummy nibh euismod tincidunt ut laoreet dolore magna aliquam erat volutpat. Ut wisi enim ad minim veniam, quis nostrud exerci tation ullamcorper suscipit lobortis nisl ut aliquip ex ea commodo consequat.<br><br>Lorem ipsum dolor sit amet, consectetuer adipiscing elit, sed diam nonummy nibh euismod tincidunt ut laoreet dolore magna aliquam erat volutpat.</div>
  <div class="abs blue" style="left:32px;top:110px;font-size:3.2px">LOREM IPSUM</div>
  <div class="abs blue" style="left:72px;top:110px;font-size:3.2px">LOREM IPSUM</div>
  <svg class="abs" style="left:0;top:0" width="278" height="156" viewBox="0 0 278 156">
    <circle cx="43" cy="130" r="13" fill="none" stroke="#ddd" stroke-width="1.5"/>
    <path d="M43 117 A13 13 0 1 0 56 130" fill="none" stroke="#1588d2" stroke-width="1.5"/>
    <circle cx="82" cy="130" r="13" fill="none" stroke="#ddd" stroke-width="1.5"/>
    <path d="M82 117 A13 13 0 1 0 95 130" fill="none" stroke="#1588d2" stroke-width="1.5"/>
    <g font-family="Poppins" font-size="5.5" font-weight="500" letter-spacing="1"><text x="33" y="132">4356</text><text x="72" y="132">2164</text></g>
    <g stroke="#ddd" stroke-width=".3"><path d="M169 27h90M169 35h90M169 43h90M169 51h90M169 59h90M169 67h90M169 75h90M169 83h90"/><path d="M177 25v60M186 25v60M195 25v60M204 25v60M213 25v60M222 25v60M231 25v60M240 25v60M249 25v60"/></g>
    <path d="M169 25v60h90" fill="none" stroke="#111" stroke-width=".6"/>
    <path d="M169 83 C180 45 190 45 200 43 S230 38 245 33" fill="none" stroke="#111" stroke-width=".8"/>
    <path d="M169 83 C178 55 190 50 200 52 S230 50 245 62" fill="none" stroke="#1588d2" stroke-width=".8"/>
    <path d="M169 83 C178 60 190 60 205 57 S235 48 245 38" fill="none" stroke="#1588d2" stroke-width=".8"/>
    <path d="M169 83 C178 70 195 65 210 70 S235 60 245 52" fill="none" stroke="#111" stroke-width=".6"/>
    <rect x="192" y="29" width="17" height="6" fill="#111"/><text x="195" y="34" font-family="Poppins" font-size="4" fill="#fff">TEXT</text>
    <g class="chart-label" font-size="3"><text x="145" y="92">1000</text><text x="147" y="100">700</text><text x="147" y="108">500</text><text x="147" y="116">300</text><text x="147" y="124">100</text><text x="149" y="132">0</text></g>
    <path d="M155 134 C165 126 170 126 175 130 S185 115 190 118 S200 126 205 124 S215 100 220 101 S228 125 240 126 L245 134 Z" fill="#1588d2"/>
    <g font-family="Poppins" font-size="3.3" font-style="normal" fill="#111"><text x="163" y="122">100</text><text x="175" y="127">20</text><text x="188" y="111">275</text><text x="206" y="119">130</text><text x="215" y="98">650</text><text x="236" y="122">80</text></g>
  </svg>
  <div class="foot"><span class="mark"></span>TAVOLIN<span class="pg">08</span></div>
</section>

<section class="slide" style="left:605px;top:356px">
  <div class="abs h-sm" style="left:17px;top:15px">ACTIVE</div>
  <div class="abs blue" style="left:17px;top:24px;font-size:9.5px;font-weight:700">INTELLIGENCE</div>
  <div class="abs body" style="left:17px;top:37px;width:90px">Lorem ipsum dolor sit amet, consectetuer adipiscing elit, sed diam nonummy nibh euismod tincidunt ut laoreet dolore magna aliquam erat volutpat. Ut wisi enim ad minim veniam, quis nostrud exerci tation ullamcorper suscipit lobortis nisl ut aliquip ex ea commodo consequat. Duis autem vel eum iriure dolor in vulputate velit esse.<br><br>Lorem ipsum dolor sit amet, consectetuer adipiscing elit, sed diam nonummy nibh euismod tincidunt ut laoreet dolore magna aliquam erat volutpat. Ut wisi enim ad minim veniam.</div>
  <div class="abs body" style="left:17px;top:101px;width:90px">▸ Lorem ipsum dolor sit amet, consectetuer adipiscing elit, sed diam nonummy nibh euismod tincidunt.</div>
  <div class="abs body" style="left:17px;top:115px;width:90px">▹ Lorem ipsum dolor sit amet, consectetuer adipiscing elit, sed diam nonummy nibh euismod tincidunt.</div>
  <div class="abs" style="left:233px;top:15px;width:33px;height:4px;background:var(--blue)"></div>
  <div class="abs" style="left:124px;top:32px;width:5px;height:100px;background:var(--blue)"></div>
  <div class="photo photo-blue" role="img" aria-label="Laptop and tablet on a desk with glowing network graphics" style="left:126px;top:23px;width:140px;height:100px"></div>
  <div class="dots dark" style="left:135px;top:18px;width:22px"></div>
  <div class="dots dark" style="left:97px;top:135px;width:22px"></div>
  <div class="foot"><span class="mark"></span>TAVOLIN<span class="pg">09</span></div>
</section>

<!-- Row 4 -->
<section class="slide" style="left:25px;top:522px">
  <div class="corner-black-top"></div>
  <div class="tab-right" style="top:30px"></div>
  <div class="dots dark" style="left:228px;top:12px;width:22px"></div>
  <div class="abs" style="left:16px;top:21px;width:117px">
    <div class="h-sm">LOREM IPSUM</div><div class="blue" style="font-size:9px;font-weight:700">DOLOR SIT AMET</div>
    <div class="body" style="margin-top:4px;text-align:justify">Lorem ipsum dolor sit amet, consectetuer adipiscing elit, sed diam nonummy nibh euismod tincidunt ut laoreet dolore magna aliquam erat volutpat. Ut wisi enim ad minim veniam, quis nostrud exerci tation ullamcorper suscipit lobortis nisl ut aliquip ex ea commodo consequat. Duis autem vel eum iriure dolor in hendrerit in vulputate velit esse.<br><br>Lorem ipsum dolor sit amet, consectetuer adipiscing elit, sed diam nonummy nibh euismod tincidunt ut laoreet dolore magna aliquam erat volutpat. Ut wisi enim ad minim veniam, quis nostrud exerci tation ullamcorper suscipit lobortis nisl ut aliquip ex ea commodo consequat. Duis autem vel eum iriure dolor in hendrerit in vulputate velit esse.</div>
    <div class="body" style="margin-top:6px">▸ Lorem ipsum dolor sit amet, consectetuer adipiscing elit, sed diam nonummy nibh euismod tincidunt ut laoreet dolore magna</div>
    <div class="body" style="margin-top:8px">▹ Lorem ipsum dolor sit amet, consectetuer adipiscing elit, sed diam nonummy nibh euismod tincidunt ut laoreet dolore magna</div>
  </div>
  <div class="abs" style="left:144px;top:21px;width:117px">
    <div class="h-sm">LOREM IPSUM</div><div class="blue" style="font-size:9px;font-weight:700">DOLOR SIT AMET</div>
    <div class="body" style="margin-top:4px;text-align:justify">Lorem ipsum dolor sit amet, consectetuer adipiscing elit, sed diam nonummy nibh euismod tincidunt ut laoreet dolore magna aliquam erat volutpat. Ut wisi enim ad minim veniam, quis nostrud exerci tation ullamcorper suscipit lobortis nisl ut aliquip ex ea commodo consequat. Duis autem vel eum iriure dolor in hendrerit in vulputate velit esse.<br><br>Lorem ipsum dolor sit amet, consectetuer adipiscing elit, sed diam nonummy nibh euismod tincidunt ut laoreet dolore magna aliquam erat volutpat. Ut wisi enim ad minim veniam, quis nostrud exerci tation ullamcorper suscipit lobortis nisl ut aliquip ex ea commodo consequat. Duis autem vel eum iriure dolor in hendrerit in vulputate velit esse.</div>
    <div class="body" style="margin-top:6px">▸ Lorem ipsum dolor sit amet, consectetuer adipiscing elit, sed diam nonummy nibh euismod tincidunt ut laoreet dolore magna</div>
    <div class="body" style="margin-top:8px">▹ Lorem ipsum dolor sit amet, consectetuer adipiscing elit, sed diam nonummy nibh euismod tincidunt ut laoreet dolore magna</div>
  </div>
  <div class="band-blue-bottom"></div>
  <div class="foot"><span class="mark"></span>TAVOLIN<span class="pg">10</span></div>
</section>

<section class="slide" style="left:315px;top:522px">
  <div class="photo photo-grey" role="img" aria-label="Faded photo of a person using a phone and card" style="left:0;top:0;width:278px;height:156px"></div>
  <div class="abs" style="left:0;bottom:0;width:12px;height:60px;background:var(--blue);border-top-right-radius:10px"></div>
  <div class="abs" style="right:0;top:0;width:12px;height:70px;background:var(--ink);border-bottom-left-radius:10px"></div>
  <div class="dots" style="left:192px;top:20px"></div>
  <div class="dots" style="left:60px;top:118px"></div>
  <div class="abs" style="left:113px;top:25px;width:60px;height:60px;border:4px solid var(--blue);border-radius:50%"></div>
  <div class="abs big-num" style="left:127px;top:37px">02</div>
  <div class="abs part" style="left:100px;top:110px">Part Two.</div>
  <div class="foot"><span class="mark"></span>TAVOLIN<span class="pg">11</span></div>
</section>

<section class="slide" style="left:605px;top:522px">
  <div class="photo photo-device" role="img" aria-label="Three smartphones showing app screens over an angular blue and black frame" style="left:8px;top:16px;width:125px;height:130px;background:linear-gradient(135deg,#1588d2,#111 55%,#f2f2f2)"></div>
  <div class="abs" style="left:145px;top:50px;font-size:16px;font-weight:700">USE <span class="blue">CASES</span></div>
  <div class="abs body" style="left:145px;top:71px;width:115px">Lorem ipsum dolor sit amet, consectetuer adipiscing elit, sed diam nonummy nibh euismod tincidunt ut laoreet dolore magna aliquam erat volutpat. Ut wisi enim ad minim veniam, quis nostrud exerci tation ullamcorper suscipit lobortis nisl ut aliquip ex ea commodo consequat. Duis autem vel eum iriure dolor in hendrerit.<br><br>Lorem ipsum dolor sit amet, consectetuer adipiscing elit, sed diam nonummy nibh euismod tincidunt ut laoreet dolore magna aliquam erat volutpat. Ut wisi enim ad minim veniam, quis nostrud exerci tation ullamcorper suscipit lobortis nisl ut aliquip ex ea commodo consequat.</div>
  <div class="tab-right"></div>
  <div class="dots dark" style="left:232px;top:8px;width:22px"></div>
  <div class="foot"><span class="mark"></span>TAVOLIN<span class="pg">12</span></div>
</section>

<!-- Row 5 -->
<section class="slide" style="left:25px;top:690px">
  <svg class="abs" style="left:0;top:0" width="278" height="156" viewBox="0 0 278 156">
    <path d="M244 122 V140 H150 C110 140 120 120 145 118 C165 116 160 102 140 98 C125 95 150 84 170 80 V62 C160 52 140 58 130 48" fill="none" stroke="#1588d2" stroke-width="1.3" stroke-dasharray="0"/>
    <path d="M244 82 V122" stroke="#111" stroke-width="1" stroke-dasharray="1.5 1.5"/>
    <path d="M190 42 V60" stroke="#111" stroke-width="1" stroke-dasharray="1.5 1.5"/>
    <path d="M145 98 V118" stroke="#111" stroke-width="1" stroke-dasharray="1.5 1.5"/>
    <circle cx="244" cy="140" r="1.6" fill="#111"/>
    <circle cx="244" cy="70" r="19" fill="#111"/><circle cx="244" cy="70" r="15" fill="#fff" stroke="#1588d2" stroke-width="1"/>
    <text x="238" y="79" font-family="Poppins" font-size="24" font-weight="700" fill="#1588d2">1</text>
    <circle cx="145" cy="87" r="9" fill="#111"/><circle cx="145" cy="87" r="7" fill="#fff"/><text x="140" y="91.5" font-family="Poppins" font-size="12" font-weight="700" fill="#1588d2">2</text>
    <circle cx="190" cy="35" r="7" fill="#111"/><circle cx="190" cy="35" r="5.5" fill="#fff"/><text x="187" y="38.5" font-family="Poppins" font-size="9" font-weight="700" fill="#1588d2">3</text>
    <circle cx="109" cy="42" r="5" fill="#111"/><circle cx="109" cy="42" r="3.8" fill="#fff"/><text x="107" y="44.5" font-family="Poppins" font-size="6.5" font-weight="700" fill="#1588d2">4</text>
    <circle cx="130" cy="28" r="4" fill="#111"/><circle cx="130" cy="28" r="3" fill="#fff"/><text x="128.5" y="30" font-family="Poppins" font-size="5" font-weight="700" fill="#1588d2">5</text>
    <circle cx="90" cy="30" r="3" fill="#111"/><circle cx="90" cy="30" r="2.2" fill="#fff"/><text x="89" y="31.5" font-family="Poppins" font-size="3.5" font-weight="700" fill="#1588d2">6</text>
  </svg>
  <div class="abs" style="left:52px;top:28px;width:36px"><div class="item-title" style="font-size:3.8px">LOREM IPSUM</div><div class="body" style="font-size:2.2px;line-height:2.8px">Lorem ipsum dolor sit amet, consectetuer adipiscing elit, sed diam nonummy nibh.</div></div>
  <div class="abs" style="left:139px;top:24px;width:36px"><div class="item-title" style="font-size:3.8px">LOREM IPSUM</div><div class="body" style="font-size:2.2px;line-height:2.8px">Lorem ipsum dolor sit amet, consectetuer adipiscing elit, sed diam nonummy nibh.</div></div>
  <div class="abs" style="left:201px;top:26px;width:36px"><div class="item-title" style="font-size:3.8px">LOREM IPSUM</div><div class="body" style="font-size:2.2px;line-height:2.8px">Lorem ipsum dolor sit amet, consectetuer adipiscing elit, sed diam nonummy nibh.</div></div>
  <div class="abs" style="left:99px;top:65px;width:36px"><div class="item-title" style="font-size:3.8px">LOREM IPSUM</div><div class="body" style="font-size:2.2px;line-height:2.8px">Lorem ipsum dolor sit amet, consectetuer adipiscing elit, sed diam nonummy nibh.</div></div>
  <div class="abs" style="left:190px;top:86px;width:36px"><div class="item-title" style="font-size:3.8px">LOREM IPSUM</div><div class="body" style="font-size:2.2px;line-height:2.8px">Lorem ipsum dolor sit amet, consectetuer adipiscing elit, sed diam nonummy nibh.</div></div>
  <div class="abs" style="left:14px;top:76px;font-size:8px;letter-spacing:1.2px">TIMELINE OF</div>
  <div class="abs blue" style="left:14px;top:84px;font-size:12px;font-weight:700">ROADMAP</div>
  <div class="abs" style="left:15px;top:99px;font-size:6px;font-weight:600">FOR 2 YEARS</div>
  <div class="abs" style="left:15px;top:117px;width:14px;height:14px;border-radius:50%;background:var(--blue);color:#fff;font-size:9px;font-weight:700;text-align:center;line-height:14px">A</div>
  <div class="abs" style="left:33px;top:117px;font-size:7px;font-weight:600;line-height:1">2019</div>
  <div class="abs body" style="left:33px;top:125px;width:32px;font-size:2.2px;line-height:2.8px">Lorem ipsum dolor sit amet, consectetuer adipiscing elit, sed diam</div>
  <div class="abs" style="left:77px;top:117px;width:14px;height:14px;border-radius:50%;background:var(--blue);color:#fff;font-size:9px;font-weight:700;text-align:center;line-height:14px">B</div>
  <div class="abs" style="left:95px;top:117px;font-size:7px;font-weight:600;line-height:1">2020</div>
  <div class="abs body" style="left:95px;top:125px;width:32px;font-size:2.2px;line-height:2.8px">Lorem ipsum dolor sit amet, consectetuer adipiscing elit, sed diam</div>
  <div class="tab-right" style="top:25px"></div>
  <div class="dots" style="left:232px;top:6px;width:22px"></div>
  <div class="corner-black"></div>
  <div class="foot"><span class="mark"></span>TAVOLIN<span class="pg">13</span></div>
</section>

<section class="slide" style="left:315px;top:690px">
  <div class="abs" style="left:0;top:13px;width:145px;height:143px;background:var(--blue);border-top-right-radius:22px"></div>
  <div class="abs white" style="left:10px;top:23px;font-size:10px;line-height:1">LOREM IPSUM</div>
  <div class="abs" style="left:10px;top:34px;font-size:10px;font-weight:800">DOLOR SIT AMET</div>
  <div class="abs body white" style="left:10px;top:49px;width:122px;text-align:justify">Lorem ipsum dolor sit amet, consectetuer adipiscing elit, sed diam nonummy nibh euismod tincidunt ut laoreet dolore magna aliquam erat volutpat. Ut wisi enim ad minim veniam, quis nostrud exerci tation ullamcorper suscipit lobortis nisl ut aliquip ex ea commodo consequat. Duis autem vel eum iriure dolor in hendrerit in vulputate velit esse molestie consequat, vel illum dolore eu feugiat nulla facilisis at vero eros et accumsan et iusto odio dignissim qui blandit praesent luptatum zzril delenit augue duis dolore te feugait nulla facilisi.<br><br>Lorem ipsum dolor sit amet, cons ectetuer adipiscing elit, sed diam nonummy nibh euismod tincidunt ut laoreet dolore magna aliquam erat volutpat. Ut wisi enim ad minim veniam, quis nostrud exerci tation ullamcorper suscipit lobortis nisl ut aliquip ex ea commodo consequat.<br><br>Lorem ipsum dolor sit amet, consectetuer adipiscing elit, sed diam nonummy nibh euismod tincidunt ut laoreet dolore magna aliquam erat volutpat. Ut wisi enim ad minim veniam, quis nostrud exerci tation ullamcorper suscipit lobortis nisl ut aliquip ex ea commodo consequat. Duis autem vel eum iriure dolor in hendrerit in vulputate velit esse molestie consequat, vel illum dolore eu feugiat nulla facilisis at vero eros et</div>
  <div class="abs" style="left:153px;top:28px;width:108px;display:grid;grid-template-columns:1fr 1fr;gap:8px 4px;text-align:center">
    <div><div style="width:20px;height:20px;margin:0 auto 3px;border-radius:50%;border:1px solid var(--blue-soft)"></div><div class="item-title" style="font-size:4px">LOREM IPSUM</div><div class="body" style="font-size:2.3px;line-height:3px">Lorem ipsum dolor sit amet, consectetuer adipiscing elit, sed diam nonummy nibh euismod tincid</div></div>
    <div><div style="width:20px;height:20px;margin:0 auto 3px;border-radius:50%;border:1px solid var(--blue-soft)"></div><div class="item-title" style="font-size:4px">LOREM IPSUM</div><div class="body" style="font-size:2.3px;line-height:3px">Lorem ipsum dolor sit amet, consectetuer adipiscing elit, sed diam nonummy nibh euismod tincid</div></div>
    <div><div style="width:20px;height:20px;margin:0 auto 3px;border-radius:50%;border:1px solid var(--blue-soft)"></div><div class="item-title" style="font-size:4px">LOREM IPSUM</div><div class="body" style="font-size:2.3px;line-height:3px">Lorem ipsum dolor sit amet, consectetuer adipiscing elit, sed diam nonummy nibh euismod tincid</div></div>
    <div><div style="width:20px;height:20px;margin:0 auto 3px;border-radius:50%;border:1px solid var(--blue-soft)"></div><div class="item-title" style="font-size:4px">LOREM IPSUM</div><div class="body" style="font-size:2.3px;line-height:3px">Lorem ipsum dolor sit amet, consectetuer adipiscing elit, sed diam nonummy nibh euismod tincid</div></div>
  </div>
  <div class="dots" style="left:222px;top:8px"></div>
  <div class="tab-right" style="top:60px"></div>
  <div class="foot"><span class="mark"></span>TAVOLIN<span class="pg">14</span></div>
</section>

<section class="slide" style="left:605px;top:690px">
  <div class="abs" style="left:22px;top:21px;font-size:10px;line-height:1">LOREM IPSUM</div>
  <div class="abs blue" style="left:22px;top:32px;font-size:10px;font-weight:700">DOLOR SIT AMET</div>
  <svg class="abs" style="left:0;top:0" width="278" height="156" viewBox="0 0 278 156">
    <path d="M58 56 A35 35 0 0 1 91 68 L78 79 A18 18 0 0 0 58 73 Z" fill="#111"/>
    <path d="M91 68 A35 35 0 0 1 91 114 L78 103 A18 18 0 0 0 78 79 Z" fill="#1588d2"/>
    <path d="M91 114 A35 35 0 0 1 44 123 L52 108 A18 18 0 0 0 78 103 Z" fill="#111"/>
    <path d="M44 123 A35 35 0 0 1 58 56 L58 73 A18 18 0 0 0 52 108 Z" fill="#1588d2"/>
    <g font-family="Poppins" font-weight="700" font-size="5.5" fill="#fff"><text x="60" y="68">27%</text><text x="82" y="95">27%</text><text x="60" y="121">32%</text><text x="27" y="97">48%</text></g>
    <text x="48" y="88" font-family="Poppins" font-weight="600" font-size="4">Your Text</text>
    <g fill="#1588d2"><rect x="54" y="92" width="2" height="6"/><rect x="57" y="90" width="2" height="8"/><rect x="60" y="93" width="2" height="5"/><rect x="63" y="91" width="2" height="7"/></g>
    <path d="M84 63h75l6 5-6 5H84z" fill="#111"/>
    <path d="M94 76h65l6 5-6 5H94z" fill="#1588d2"/>
    <path d="M94 89h65l6 5-6 5H94z" fill="#111"/>
    <path d="M92 102h67l6 5-6 5H92z" fill="#1588d2"/>
    <g font-family="Poppins" font-weight="600" font-size="4" fill="#fff" text-anchor="end"><text x="145" y="70">Analysis</text><text x="145" y="83">Communication</text><text x="145" y="96">Recruitment</text><text x="145" y="109">Planning</text></g>
    <g fill="#fff"><circle cx="154" cy="68" r="2"/><circle cx="154" cy="81" r="2"/><circle cx="154" cy="94" r="2"/><rect x="152" y="105" width="4" height="4"/></g>
  </svg>
  <div class="abs" style="left:178px;top:24px;width:80px">
    <div class="item-title" style="font-size:4.5px">LOREM IPSUM</div><div class="body">Lorem ipsum dolor sit amet, consectetuer adipiscing elit, sed diam nonummy nibh euismod tincid</div>
    <div class="item-title blue" style="font-size:4.5px;margin-top:5px">LOREM IPSUM</div><div class="body">Lorem ipsum dolor sit amet, consectetuer adipiscing elit, sed diam nonummy nibh euismod tincid</div>
    <div class="item-title" style="font-size:4.5px;margin-top:5px">LOREM IPSUM</div><div class="body">Lorem ipsum dolor sit amet, consectetuer adipiscing elit, sed diam nonummy nibh euismod tincid</div>
    <div class="item-title blue" style="font-size:4.5px;margin-top:5px">LOREM IPSUM</div><div class="body">Lorem ipsum dolor sit amet, consectetuer adipiscing elit, sed diam nonummy nibh euismod tincid</div>
  </div>
  <div class="abs" style="right:0;top:0;width:11px;height:45px;background:var(--ink)"></div>
  <div class="abs" style="left:0;bottom:0;width:50px;height:8px;background:var(--blue);border-top-right-radius:8px"></div>
  <div class="foot"><span class="mark"></span>TAVOLIN<span class="pg">15</span></div>
</section>

<!-- Row 6 -->
<section class="slide" style="left:25px;top:856px">
  <div class="abs" style="left:49px;top:26px;font-size:10px;letter-spacing:2.5px;font-weight:500">TIMELINE <span style="background:var(--blue);color:#fff;font-weight:700;padding:0 2px">INFOGRAPHIC</span></div>
  <svg class="abs" style="left:0;top:0" width="278" height="156" viewBox="0 0 278 156">
    <path d="M23 80h51l5 6-5 6H23l4-6z" fill="#111"/>
    <path d="M80 80h51l5 6-5 6H80l4-6z" fill="#1588d2"/>
    <path d="M137 80h51l5 6-5 6h-51l4-6z" fill="#111"/>
    <path d="M194 80h51l5 6-5 6h-51l4-6z" fill="#1588d2"/>
    <g font-family="Poppins" font-weight="700" font-size="7.5" fill="#fff"><text x="41" y="89">2018</text><text x="98" y="89">2019</text><text x="155" y="89">2020</text><text x="212" y="89">2021</text></g>
    <g fill="none" stroke="#1588d2" stroke-width=".8"><path d="M40 80V66h-1"/><path d="M155 80V66"/><path d="M118 92v14h-7"/><path d="M235 92v14h-7"/></g>
    <g fill="#fff" stroke="#1588d2" stroke-width="1"><circle cx="41" cy="63" r="2.5"/><circle cx="156" cy="63" r="2.5"/><circle cx="108" cy="106" r="2.5"/><circle cx="225" cy="106" r="2.5"/></g>
  </svg>
  <div class="abs blue" style="left:23px;top:61px;font-size:4.5px;font-weight:600">TEXT</div>
  <div class="abs body" style="left:23px;top:67px;width:32px;font-size:2.2px;line-height:2.8px">Lorem ipsum dolor sit amet, consectetuer adipiscing elit, sed diam tempor incidunt</div>
  <div class="abs blue" style="left:138px;top:61px;font-size:4.5px;font-weight:600">TEXT</div>
  <div class="abs body" style="left:138px;top:67px;width:32px;font-size:2.2px;line-height:2.8px">Lorem ipsum dolor sit amet, consectetuer adipiscing elit, sed diam tempor incidunt</div>
  <div class="abs blue" style="left:85px;top:74px;font-size:3.8px;font-weight:600">TEXT | LOREM IPSUM</div>
  <div class="abs blue" style="left:200px;top:74px;font-size:3.8px;font-weight:600">TEXT | LOREM IPSUM</div>
  <div class="abs" style="left:27px;top:96px;font-size:3.8px;font-weight:600">TEXT | LOREM IPSUM</div>
  <div class="abs" style="left:142px;top:96px;font-size:3.8px;font-weight:600">TEXT | LOREM IPSUM</div>
  <div class="abs" style="left:92px;top:104px;font-size:4.5px;font-weight:600">TEXT</div>
  <div class="abs body" style="left:93px;top:110px;width:32px;font-size:2.2px;line-height:2.8px">Lorem ipsum dolor sit amet, consectetuer adipiscing elit, sed diam tempor incidunt</div>
  <div class="abs" style="left:209px;top:104px;font-size:4.5px;font-weight:600">TEXT</div>
  <div class="abs body" style="left:210px;top:110px;width:32px;font-size:2.2px;line-height:2.8px">Lorem ipsum dolor sit amet, consectetuer adipiscing elit, sed diam tempor incidunt</div>
  <div class="abs" style="right:0;top:0;width:11px;height:55px;background:var(--ink);border-bottom-left-radius:10px"></div>
  <div class="dots" style="left:230px;top:8px;width:22px"></div>
  <div class="band-blue-bottom" style="width:58px"></div>
  <div class="foot"><span class="mark"></span>TAVOLIN<span class="pg">16</span></div>
</section>

<section class="slide" style="left:315px;top:856px">
  <div class="abs" style="left:0;top:0;width:145px;height:142px;background:var(--blue);border-bottom-right-radius:22px"></div>
  <div class="abs white" style="left:10px;top:9px;font-size:10px;line-height:1">LOREM IPSUM</div>
  <div class="abs" style="left:10px;top:20px;font-size:10px;font-weight:800">DOLOR SIT AMET</div>
  <div class="abs body white" style="left:10px;top:35px;width:122px;text-align:justify">Lorem ipsum dolor sit amet, consectetuer adipiscing elit, sed diam nonummy nibh euismod tincidunt ut laoreet dolore magna aliquam erat volutpat. Ut wisi enim ad minim veniam, quis nostrud exerci tation ullamcorper suscipit lobortis nisl ut aliquip ex ea commodo consequat. Duis autem vel eum iriure dolor in hendrerit in vulputate velit esse molestie consequat, vel illum dolore eu feugiat nulla facilisis at vero eros et accumsan et iusto odio dignissim.<br><br>Lorem ipsum dolor sit amet, cons ectetuer adipiscing elit, sed diam nonummy nibh euismod tincidunt ut laoreet dolore magna aliquam erat volutpat. Ut wisi enim ad minim veniam, quis nostrud exerci tation ullamcorper suscipit lobortis nisl ut aliquip ex ea commodo consequat.<br><br>Lorem ipsum dolor sit amet, consectetuer adipiscing elit, sed diam nonummy nibh euismod tincidunt ut laoreet dolore magna aliquam erat volutpat. Ut wisi enim ad minim veniam, quis nostrud exerci tation ullamcorper suscipit lobortis nisl ut aliquip ex ea commodo consequat. Duis autem vel eum iriure dolor in hendrerit in vulputate velit esse molestie consequat.</div>
  <div class="dots dark" style="left:17px;top:128px;width:22px"></div>
  <div class="photo" role="img" aria-label="Illustration of a team meeting around a table with a growth chart" style="left:150px;top:25px;width:112px;height:110px;background:linear-gradient(180deg,var(--blue-mist),#d6e6f3 60%,#9fc3e2)"></div>
  <div class="tab-right" style="top:20px"></div>
  <div class="foot"><span class="mark"></span>TAVOLIN<span class="pg">17</span></div>
</section>

<section class="slide" style="left:605px;top:856px">
  <div class="corner-black-top"></div>
  <div class="tab-right" style="top:20px"></div>
  <div class="dots dark" style="left:226px;top:10px;width:28px"></div>
  <div class="abs" style="left:6px;top:120px;width:5px;height:18px;background:var(--blue)"></div>
  <div class="photo photo-grey" role="img" aria-label="Black and white photo of colleagues smiling at a computer" style="left:14px;top:26px;width:118px;height:112px"></div>
  <div class="abs" style="left:134px;top:26px;font-size:9px;line-height:1">BENEFITS TO EACH</div>
  <div class="abs blue" style="left:134px;top:36px;font-size:9px;font-weight:700">CUSTOMER SEGMENTS</div>
  <div class="abs body" style="left:134px;top:50px;width:125px;text-align:justify">Lorem ipsum dolor sit amet, consectetuer adipiscing elit, sed diam nonummy nibh euismod tincidunt ut laoreet dolore magna aliquam erat volutpat. Ut wisi enim ad minim veniam, quis nostrud exerci tation ullam<br><br>Lorem ipsum dolor sit amet, consectetuer adipiscing elit, sed diam nonummy nibh euismod tincidunt ut laoreet dolore magna aliquam erat volutpat. Ut wisi enim ad minim veniam, quis nostrud exerci tation ullam<br><br>Lorem ipsum dolor sit amet, consectetuer adipiscing elit, sed diam nonummy nibh euismod tincidunt ut laoreet dolore magna aliquam erat volutpat. Ut wisi enim ad minim veniam, quis nostrud exerci tation ullam<br>Lorem ipsum dolor sit amet, consectetuer adipiscing elit, sed diam nonummy nibh euismod tincidunt ut laoreet dolore magna aliquam erat volutpat. Ut wisi enim ad minim veniam, quis nostrud exerci</div>
  <div class="foot"><span class="mark"></span>TAVOLIN<span class="pg">18</span></div>
</section>

<!-- Row 7 -->
<section class="slide" style="left:25px;top:1023px">
  <div class="tab-left" style="top:0;height:40px"></div>
  <div class="dots" style="left:192px;top:20px"></div>
  <div class="abs" style="left:18px;top:41px;font-size:9px;line-height:1">OUR COMPANY</div>
  <div class="abs blue" style="left:18px;top:51px;font-size:9.5px;font-weight:700">TERMS &amp; CONDITIONS</div>
  <div class="abs body" style="left:18px;top:65px;width:115px">Lorem ipsum dolor sit amet, consectetuer adipiscing elit, sed diam nonummy nibh euismod tincidunt ut laoreet dolore magna aliquam erat volutpat. Ut wisi enim ad minim veniam, quis nostrud exerci tation ullam<br><br>Lorem ipsum dolor sit amet, consectetuer adipiscing elit, sed diam nonummy nibh euismod tincidunt ut laoreet dolore magna aliquam erat volutpat. Ut wisi enim ad minim veniam, quis nostrud exerci tation ullam<br><br>Lorem ipsum dolor sit amet, consectetuer adipiscing elit, sed diam nonummy nibh euismod tincidunt ut laoreet dolore magna aliquam erat volutpat. Ut wisi enim ad minim veniam, quis nostrud</div>
  <div class="photo photo-device" role="img" aria-label="Laptop showing an illustration of a team at a meeting table" style="left:138px;top:40px;width:126px;height:72px;border-radius:4px;background:linear-gradient(180deg,#2b2b2b,#e8f1f8 15%,#cadeef 80%,#9a9a9a)"></div>
  <div class="dots" style="left:125px;top:116px;width:22px"></div>
  <div class="band-blue-bottom" style="left:25px;width:96px;border-radius:8px 8px 0 0"></div>
  <div class="foot"><span class="mark"></span>TAVOLIN<span class="pg">19</span></div>
</section>

<section class="slide" style="left:315px;top:1023px">
  <div class="corner-black-tr" style="width:58px"></div>
  <div class="abs" style="left:0;top:0;width:278px;text-align:center;top:23px;font-size:9px">TEAM MEMBERS <span class="blue" style="font-weight:700">AND ADVISORS</span></div>
  <div class="abs body" style="left:18px;top:35px;width:242px;text-align:center">Lorem ipsum dolor sit amet, consectetuer adipiscing elit, sed diam nonummy nibh euismod tincidunt ut laoreet dolore magna aliquam erat volutpat. Ut wisi enim ad minim veniam, quis nostrud exerci tation ullamcorper suscipit lobortis nisl ut aliquip ex ea commodo consequat. Duis autem<br><br>Lorem ipsum dolor sit amet, cons ectetuer adipiscing elit, sed diam nonummy nibh euismod tincidunt ut laoreet dolore magna aliquam erat volutpat.</div>
  <div class="abs" style="left:0;top:64px;width:278px;height:75px;background:var(--blue)"></div>
  <div class="abs" style="left:0;top:69px;width:278px;display:grid;grid-template-columns:repeat(4,1fr);padding:0 18px;gap:8px;text-align:center">
    <div><div role="img" aria-label="Team member portrait" style="width:24px;height:24px;margin:0 auto;border-radius:50%;background:var(--blue-pale);border:2px solid var(--white)"></div><div style="font-size:4.5px;font-weight:700;margin-top:2px">DANA REYES</div><div class="body white" style="font-size:2.2px;line-height:2.8px">Lorem ipsum dolor sit amet, consectetuer adipiscing elit, sed diam nonummy nibh euismod tincidunt ut laoreet dolore magna aliquam erat volutpat.</div></div>
    <div><div role="img" aria-label="Team member portrait" style="width:24px;height:24px;margin:0 auto;border-radius:50%;background:var(--blue-pale);border:2px solid var(--white)"></div><div style="font-size:4.5px;font-weight:700;margin-top:2px">LENA ORTIZ</div><div class="body white" style="font-size:2.2px;line-height:2.8px">Lorem ipsum dolor sit amet, consectetuer adipiscing elit, sed diam nonummy nibh euismod tincidunt ut laoreet dolore magna aliquam erat volutpat.</div></div>
    <div><div role="img" aria-label="Team member portrait" style="width:24px;height:24px;margin:0 auto;border-radius:50%;background:var(--blue-pale);border:2px solid var(--white)"></div><div style="font-size:4.5px;font-weight:700;margin-top:2px">DANA REYES</div><div class="body white" style="font-size:2.2px;line-height:2.8px">Lorem ipsum dolor sit amet, consectetuer adipiscing elit, sed diam nonummy nibh euismod tincidunt ut laoreet dolore magna aliquam erat volutpat.</div></div>
    <div><div role="img" aria-label="Team member portrait" style="width:24px;height:24px;margin:0 auto;border-radius:50%;background:var(--blue-pale);border:2px solid var(--white)"></div><div style="font-size:4.5px;font-weight:700;margin-top:2px">LENA ORTIZ</div><div class="body white" style="font-size:2.2px;line-height:2.8px">Lorem ipsum dolor sit amet, consectetuer adipiscing elit, sed diam nonummy nibh euismod tincidunt ut laoreet dolore magna aliquam erat volutpat.</div></div>
  </div>
  <div class="corner-black"></div>
  <div class="foot"><span class="mark"></span>TAVOLIN<span class="pg">20</span></div>
</section>

<section class="slide" style="left:605px;top:1023px">
  <div class="abs" style="left:0;top:18px;width:160px;height:138px;background:var(--blue);border-top-left-radius:45px;border-top-right-radius:45px"></div>
  <div class="abs" style="left:18px;bottom:8px;font-size:5.5px;letter-spacing:2px;color:var(--white)">www.tavolin.com</div>
  <div class="dots" style="left:22px;top:80px;background-image:radial-gradient(circle,#fff .6px,transparent .8px)"></div>
  <div class="abs" style="left:168px;top:62px;display:flex;align-items:center;gap:4px">
    <span style="width:7px;height:7px;background:var(--blue)"></span>
    <span style="font-size:18px;font-weight:700">TAVOLIN</span>
  </div>
  <div class="abs" style="left:169px;top:97px;font-size:8px;font-weight:700">CONTACT <span class="blue">US</span></div>
  <div class="abs" style="left:169px;top:109px;font-size:5px;line-height:7px">
    <div><span class="blue">●</span> 555-014-0199</div>
    <div><span class="blue">●</span> hello@tavolin.com</div>
    <div><span class="blue">●</span> Your address, your city, box 88900</div>
  </div>
  <div class="tab-right"></div>
  <div class="dots" style="left:225px;top:20px"></div>
  <div class="dots dark" style="left:208px;top:132px;width:22px"></div>
</section>

</body>
</html>
```